mortgage company professional business card

We would like to revamp our business card. Logos and current card attached.

Target Market(s)

white collar professionals

Industry/Entity Type

Mortgage Lender

Contact Information for Business Card

Looking for a sharp professional feel with white background for business card. No gloss. Looking for emboss.

Requirements
Must have
• -Professional touch
• -Emboss and raised lettering
• -Social media icons
• name, title, Phone, email, NMLS and web
• Complement logo and web

```html
<!DOCTYPE html>
<html lang="en">
<head>
<meta charset="utf-8">
<title>Lendhaven Business Card</title>
<link rel="stylesheet" href="https://fonts.googleapis.com/css2?family=Source+Sans+3:wght@400;600;700&display=swap">
<style>
  :root {
    --page-bg: #3a3a3a;
    --card-bg: #ffffff;
    --card-edge: #dcdcdc;
    --brand-green: #2fae4a;
    --brand-blue: #2c4a9c;
    --text-dark: #333333;
    --divider: #e2e2e2;
    --social-dot: #3a3a3a;
  }
  * { box-sizing: border-box; margin: 0; padding: 0; }
  html, body { width: 1200px; height: 900px; overflow: hidden; }
  body {
    background: var(--page-bg);
    font-family: "Source Sans 3", "Myriad Pro", Arial, sans-serif;
    display: flex;
    align-items: center;
    justify-content: center;
    gap: 40px;
  }
  .card {
    width: 530px;
    height: 310px;
    background: var(--card-bg);
    border: 1px solid var(--card-edge);
    border-radius: 22px;
    position: relative;
    overflow: hidden;
  }
  /* Front */
  .card-front { display: flex; }
  .front-brand {
    width: 50%;
    display: flex;
    align-items: center;
    justify-content: center;
    gap: 12px;
  }
  .brand-square {
    width: 26px; height: 26px;
    background: var(--brand-green);
  }
  .brand-name {
    color: var(--brand-green);
    font-weight: 700;
    font-size: 34px;
    letter-spacing: 0.5px;
  }
  .front-details {
    width: 50%;
    border-left: 1px solid var(--divider);
    padding: 44px 0 0 28px;
    color: var(--text-dark);
    font-size: 15px;
    line-height: 1.3;
  }
  .person-name { color: var(--brand-green); font-weight: 600; font-size: 20px; line-height: 1.1; }
  .person-title { font-size: 15px; }
  .person-nmls { font-size: 15px; margin-bottom: 20px; }
  .address { margin-bottom: 16px; }
  .contact-list { list-style: none; }
  .contact-list li { display: flex; align-items: center; gap: 10px; margin-bottom: 2px; }
  .contact-list svg { width: 12px; height: 12px; flex: none; fill: var(--brand-green); }
  /* Back */
  .card-back {
    display: flex;
    flex-direction: column;
    align-items: center;
    justify-content: center;
    gap: 26px;
  }
  .back-brand {
    color: var(--brand-blue);
    font-weight: 700;
    font-size: 52px;
    letter-spacing: 0.5px;
  }
  .social-row { display: flex; gap: 8px; }
  .social-dot { width: 20px; height: 20px; border-radius: 50%; background: var(--social-dot); }
</style>
</head>
<body>
  <section class="card card-front">
    <div class="front-brand">
      <span class="brand-square"></span>
      <span class="brand-name">Lendhaven</span>
    </div>
    <div class="front-details">
      <p class="person-name">Owen Hartley</p>
      <p class="person-title">Managing Director</p>
      <p class="person-nmls">NMLS #482913</p>
      <p class="address">12345 Address Street City<br>State Postcode Country</p>
      <ul class="contact-list">
        <li><svg viewBox="0 0 24 24"><path d="M6.6 10.8a15 15 0 0 0 6.6 6.6l2.2-2.2a1 1 0 0 1 1-.25 11.4 11.4 0 0 0 3.6.6 1 1 0 0 1 1 1V20a1 1 0 0 1-1 1A17 17 0 0 1 3 4a1 1 0 0 1 1-1h3.5a1 1 0 0 1 1 1c0 1.25.2 2.45.6 3.6a1 1 0 0 1-.25 1z"/></svg>0800 (555) 2718</li>
        <li><svg viewBox="0 0 24 24"><path d="M2 5h20v14H2z M2 5l10 8 10-8" stroke="#ffffff" stroke-width="2"/></svg>info@lendhaven.com</li>
        <li><svg viewBox="0 0 24 24"><circle cx="12" cy="12" r="10"/></svg>www.lendhaven.com</li>
      </ul>
    </div>
  </section>

  <section class="card card-back">
    <span class="back-brand">Lendhaven</span>
    <div class="social-row" aria-label="Social media links">
      <span class="social-dot"></span>
      <span class="social-dot"></span>
      <span class="social-dot"></span>
      <span class="social-dot"></span>
      <span class="social-dot"></span>
    </div>
  </section>
</body>
</html>
```